Postcard Mailing 1

Our website is qrtechaid.net
We travel on site to help people/businesses with their computer issues.
This postcard is going to existing customers... just trying to touch them again.
QRT Technic provides a full line of residential and commercial computer support.

I've attached some stuff that I have done.

```html
<!DOCTYPE html>
<html lang="en">
<head>
<meta charset="utf-8">
<title>QRT Technic – Postcard Mailing</title>
<link rel="stylesheet" href="https://fonts.googleapis.com/css2?family=Arimo:ital,wght@0,400;0,700;1,700&family=Roboto+Condensed:ital,wght@0,400;0,700;1,700&display=swap">
<style>
  :root{
    --page:#f1ede6;
    --card:#ffffff;
    --sky:#cfe9f8;
    --sky-deep:#8fd0f0;
    --lime:#d8e63a;
    --lime-deep:#c4d92a;
    --yellow:#fff200;
    --red:#e3231b;
    --navy:#1f3f93;
    --blue:#2f5fbf;
    --ink:#1a1a1a;
    --line:#b9b9b9;
  }
  *{box-sizing:border-box;margin:0;padding:0}
  html,body{width:1200px;height:500px;overflow:hidden;background:var(--page)}
  .canvas{position:relative;width:1200px;height:500px}
  .card{position:absolute;top:24px;height:434px;background:var(--card);box-shadow:0 2px 6px rgba(0,0,0,.18);overflow:hidden}

  /* front */
  .card--front{left:22px;width:562px;
    background:linear-gradient(160deg,var(--sky) 0%,#e6f4fb 22%,#eaf1b0 42%,var(--lime) 60%,var(--lime-deep) 100%)}
  .brand{position:absolute;left:28px;top:26px;display:flex;align-items:center;gap:10px;
    font-family:"Arimo",sans-serif;font-weight:700;font-size:34px;color:var(--navy)}
  .brand__dot{width:16px;height:16px;border-radius:50%;background:var(--navy)}
  .plan{position:absolute;left:292px;top:18px;width:260px;text-align:center;font-family:"Arimo",sans-serif}
  .plan__url{color:var(--red);font-weight:700;font-size:21px}
  .plan__name{color:var(--blue);font-weight:700;font-size:17px;margin-top:5px;letter-spacing:.3px}
  .plan__pitch{color:var(--navy);font-weight:700;font-style:italic;font-size:17px;line-height:21px;margin-top:2px}
  .headline{position:absolute;left:16px;top:112px;font-family:"Arimo",sans-serif;font-weight:700;font-style:italic;
    color:var(--red);font-size:24px;line-height:30px}
  .price{position:absolute;left:364px;top:114px;width:112px;height:60px;border-radius:9px;background:var(--blue);
    color:var(--yellow);font-family:"Arimo",sans-serif;font-weight:700;font-style:italic;font-size:20px;line-height:26px;
    text-align:center;padding-top:5px}
  .services{position:absolute;left:14px;top:176px;list-style:none;font-family:"Arimo",sans-serif;font-weight:700;
    font-size:15.6px;line-height:22px;letter-spacing:-.2px;color:var(--ink)}
  .services li::before{content:"•";color:var(--red);margin-right:2px}
  .device{position:absolute;left:216px;top:200px;width:72px;height:70px;border-radius:6px;
    background:linear-gradient(135deg,#e4e4e4,#5a8fd8)}
  .features{position:absolute;left:308px;top:180px;width:230px;font-family:"Roboto Condensed",sans-serif;
    font-size:11.5px;line-height:14px;color:var(--ink)}
  .features__intro{margin-bottom:4px}
  .features ul{list-style:none}
  .features li{margin-bottom:4px}
  .features svg{vertical-align:-2px;margin-right:2px}
  .closing{position:absolute;left:10px;top:360px;width:262px;text-align:center;font-family:"Roboto Condensed",sans-serif;
    font-weight:700;font-size:12px;line-height:14px;color:var(--blue)}
  .phone{display:flex;align-items:center;gap:6px;font-family:"Arimo",sans-serif;font-weight:700;color:var(--red)}
  .phone--front{position:absolute;left:276px;top:354px;font-size:31px;letter-spacing:1px}
  .web-band{position:absolute;left:275px;top:390px;width:270px;height:28px;background:var(--red);color:#fff;
    font-family:"Arimo",sans-serif;font-weight:700;font-size:21px;text-align:center;line-height:28px}

  /* back */
  .card--back{left:616px;width:564px}
  .back-panel{position:absolute;left:14px;top:12px;width:255px;height:344px;
    background:linear-gradient(160deg,var(--sky-deep) 0%,var(--sky) 40%,#f6fbfe 100%)}
  .coupon{position:absolute;left:16px;top:13px;width:250px;height:168px;border:2px dashed var(--ink)}
  .coupon__brand{height:72px;background:#fff;display:flex;align-items:center;justify-content:center;gap:8px;
    font-family:"Arimo",sans-serif;font-weight:700;font-size:28px;color:var(--navy)}
  .coupon__brand .brand__dot{width:13px;height:13px}
  .coupon__offer{height:92px;background:var(--yellow);text-align:center;font-family:"Arimo",sans-serif;padding-top:3px}
  .coupon__call{color:var(--navy);font-weight:700;font-size:15.5px}
  .coupon__pct{color:var(--red);font-weight:700;font-size:26px;line-height:27px}
  .phone--coupon{justify-content:center;color:var(--navy);font-size:20px;letter-spacing:.5px}
  .coupon__terms{font-size:7px;line-height:8.5px;color:var(--ink);margin-top:2px}
  .burst{position:absolute;left:20px;top:191px;width:242px;height:160px}
  .burst__text{position:absolute;inset:0;display:flex;flex-direction:column;align-items:center;justify-content:center;
    font-family:"Arimo",sans-serif;font-weight:700;text-align:center}
  .burst__lead{font-size:17px;line-height:19px;color:var(--ink)}
  .burst__strong{font-size:23px;line-height:24px;color:#1aa3dc}
  .stamp{position:absolute;left:420px;top:31px;width:109px;height:107px;border:1px solid var(--line)}
  .address-line{position:absolute;left:314px;width:215px;height:1px;background:var(--line)}
</style>
</head>
<body>
<main class="canvas">

  <section class="card card--front" aria-label="Postcard front">
    <div class="brand"><span class="brand__dot"></span>QRT Technic</div>

    <div class="plan">
      <p class="plan__url">www.careplan4u.com</p>
      <p class="plan__name">EASY CARE SOLUTIONS</p>
      <p class="plan__pitch">Get More 4 Less with a<br>Managed PC Care Plan</p>
    </div>

    <h1 class="headline">Your One-Stop Computer<br>Care and Repair</h1>
    <p class="price">$19,95<br>a month</p>

    <ul class="services">
      <li>Virus/Spyware Removal</li>
      <li>Data Backup &amp; Recovery</li>
      <li>System Updates</li>
      <li>Computer Setup</li>
      <li>Wi-Fi Settings &amp; Services</li>
      <li>In-Home Service</li>
      <li>Unlimited Support</li>
      <li>Phenomenal Service Guaranteed!</li>
    </ul>

    <div class="device" role="img" aria-label="Illustration of a desktop computer with monitor and tower"></div>

    <div class="features">
      <p class="features__intro">Easy Care Solutions’ services and solutions to help you with the following:</p>
      <ul>
        <li><svg width="11" height="11" viewBox="0 0 11 11"><rect x=".5" y=".5" width="10" height="10" fill="#fff" stroke="#e3231b"/><path d="M2 5.5l2.5 2.5L10 1" fill="none" stroke="#e3231b" stroke-width="1.8"/></svg><b>PC and server repair</b> – if you have more than one piece of equipment down, we can fix anything you need to have repaired</li>
        <li><svg width="11" height="11" viewBox="0 0 11 11"><rect x=".5" y=".5" width="10" height="10" fill="#fff" stroke="#e3231b"/><path d="M2 5.5l2.5 2.5L10 1" fill="none" stroke="#e3231b" stroke-width="1.8"/></svg><b>Software and hardware upgrades</b> – when we’re done fixing your computer, we’ll update it to keep it running at its best</li>
        <li><svg width="11" height="11" viewBox="0 0 11 11"><rect x=".5" y=".5" width="10" height="10" fill="#fff" stroke="#e3231b"/><path d="M2 5.5l2.5 2.5L10 1" fill="none" stroke="#e3231b" stroke-width="1.8"/></svg><b>Lightning quick services</b> – we won’t waste your time with day-long service projects, we’ll get it done fast</li>
      </ul>
    </div>

    <p class="closing">With our easy and affordable on-site computer<br>repair services, you can expect the best out of<br>your PC network. Call us today to see how<br>we can help you</p>

    <p class="phone phone--front">
      <svg width="24" height="24" viewBox="0 0 24 24" aria-hidden="true"><circle cx="12" cy="12" r="10" fill="none" stroke="currentColor" stroke-width="2"/><path d="M9 6c-2 2-2 10 0 12l2-2c-1-2-1-6 0-8z" fill="currentColor"/></svg>
      555.013.2847
    </p>
    <p class="web-band">www.qrtechaid.net</p>
  </section>

  <section class="card card--back" aria-label="Postcard back">
    <div class="back-panel"></div>

    <div class="coupon">
      <div class="coupon__brand"><span class="brand__dot"></span>QRT Technic</div>
      <div class="coupon__offer">
        <p class="coupon__call">call us now and get</p>
        <p class="coupon__pct">20% OFF</p>
        <p class="phone phone--coupon">
          <svg width="16" height="16" viewBox="0 0 24 24" aria-hidden="true"><circle cx="12" cy="12" r="10" fill="none" stroke="currentColor" stroke-width="2"/><path d="M9 6c-2 2-2 10 0 12l2-2c-1-2-1-6 0-8z" fill="currentColor"/></svg>
          555.013.2847
        </p>
        <p class="coupon__terms">Offer not valid with any other offer or coupon.<br>Offer valid through 1/31/2015</p>
      </div>
    </div>

    <div class="burst">
      <svg width="242" height="160" viewBox="0 0 240 160" aria-hidden="true">
        <polygon fill="#e3231b" points="238,80 211.8,95 222.2,119 187.2,121 179,147.5 144.6,136 120,158 95.4,136 61,147.5 52.8,121 17.8,119 28.2,95 2,80 28.2,65 17.8,41 52.8,39 61,12.5 95.4,24 120,2 144.6,24 179,12.5 187.2,39 222.2,41 211.8,65"/>
        <polygon fill="#fff200" transform="translate(120 80) scale(.88) translate(-120 -80)" points="238,80 211.8,95 222.2,119 187.2,121 179,147.5 144.6,136 120,158 95.4,136 61,147.5 52.8,121 17.8,119 28.2,95 2,80 28.2,65 17.8,41 52.8,39 61,12.5 95.4,24 120,2 144.6,24 179,12.5 187.2,39 222.2,41 211.8,65"/>
      </svg>
      <div class="burst__text">
        <span class="burst__lead">If We Can’t<br>Fix It,</span>
        <span class="burst__strong">YOU DON’T<br>PAY</span>
      </div>
    </div>

    <div class="stamp" aria-label="Stamp area"></div>
    <div class="address-line" style="top:213px"></div>
    <div class="address-line" style="top:245px"></div>
    <div class="address-line" style="top:276px"></div>
    <div class="address-line" style="top:307px"></div>
  </section>

</main>
</body>
</html>
```